GOLD COMB label

GOLD COMB – Concept Brief

We are designing a label for our premium honey brand, GOLD COMB. Our goal is to create a bold, prestigious, and proudly African aesthetic that reflects the product's purity, ethical sourcing, and exceptional quality.

Key Design Elements:

1. Brand Name Emphasis:

The word GOLD should be large, bold, eye catching, and prominent, drawing immediate attention.

The word COMB should also be noticeable but doesn’t need to be as dominant as GOLD.

2. Visual Theme:

Incorporate African tapestry patterns, ideally within an outline of the African continent or as part of the background design.

The patterns should evoke a sense of tradition, heritage, and authenticity.

3. Text and Messaging:

A clear statement that the honey is:

Natural, raw, Organic Certified, and Ethically Produced.

Sourced from Zambia's pristine Miombo Forests.

Emphasize that this is pure, unadulterated honey of the highest quality.

4. Aesthetic and Impact:

The design should be elegant and prestigious, reinforcing the message that Africa represents quality.

Use rich, earthy tones with bold highlights to ensure the bottle stands out on the shelf and conveys purity and authenticity. Perhaps some use of gold foil in the label or logo.

5. Overall Feel:

The label should exude a sense of luxury while maintaining a strong African identity.

Balancing boldness with elegance will ensure the product feels premium yet natural.

Logo Text

GOLD COMB followed by some of the ideas above.

```html
<!DOCTYPE html>
<html lang="en">
<head>
<meta charset="utf-8">
<title>GOLD COMB label</title>
<link rel="stylesheet" href="https://fonts.googleapis.com/css2?family=Montserrat:wght@700;800&display=swap">
<style>
  :root{
    --ink:#141010;
    --ink-soft:#1e1714;
    --gold:#e9c27a;
    --gold-bright:#f4d79a;
    --gold-deep:#b98a45;
    --band-light:#ecd29b;
    --band-mid:#d9ad63;
    --rust:#8a3a1c;
    --brown:#5a3218;
  }
  html,body{margin:0;padding:0;overflow:hidden;background:var(--ink);}
  .label{
    position:relative;width:1200px;height:1200px;overflow:hidden;
    font-family:"Montserrat",sans-serif;background:var(--ink);
  }
  .shapes{position:absolute;inset:0;}
  .pattern-top{
    position:absolute;left:0;top:0;width:1200px;height:447px;
    background:linear-gradient(135deg,var(--gold-deep) 0%,var(--rust) 35%,var(--gold) 60%,var(--brown) 100%);
  }
  .pattern-bottom{
    position:absolute;left:0;top:1068px;width:1200px;height:132px;
    background:linear-gradient(90deg,var(--gold-deep),var(--gold),var(--gold-deep));
  }
  .continent-area{
    position:absolute;left:535px;top:150px;width:170px;height:185px;border-radius:40%;
    background:radial-gradient(circle,var(--gold-bright),var(--gold-deep));
  }
  .year{position:absolute;top:272px;font-weight:800;font-size:46px;color:var(--gold);}
  .year-left{left:482px;}
  .year-right{left:712px;}
  .brand{position:absolute;left:0;width:1200px;text-align:center;color:var(--gold-bright);font-weight:800;line-height:1;}
  .brand-main{top:390px;font-size:228px;letter-spacing:-4px;}
  .brand-sub{top:618px;font-size:66px;letter-spacing:3px;}
  .claim{position:absolute;font-weight:800;color:var(--ink);line-height:1.02;}
  .claim-raw{left:195px;top:690px;font-size:64px;}
  .claim-natural{left:170px;top:845px;font-size:60px;}
  .claim-organic{right:120px;top:672px;font-size:50px;text-align:center;}
  .claim-ethical{right:88px;top:830px;font-size:46px;text-align:center;}
  .origin{
    position:absolute;left:0;top:960px;width:1200px;text-align:center;
    color:var(--gold);font-weight:800;font-size:44px;line-height:1.05;
  }
</style>
</head>
<body>
<div class="label">
  <div class="pattern-top" role="img" aria-label="African tapestry pattern in gold, rust and black"></div>
  <div class="pattern-bottom" role="img" aria-label="Border of repeating African eye motifs in gold and black"></div>

  <svg class="shapes" width="1200" height="1200" viewBox="0 0 1200 1200" aria-hidden="true">
    <defs>
      <linearGradient id="band" x1="0" y1="0" x2="1" y2="0">
        <stop offset="0" stop-color="#d9ad63"/>
        <stop offset="0.5" stop-color="#ecd29b"/>
        <stop offset="1" stop-color="#d9ad63"/>
      </linearGradient>
    </defs>
    <rect class="band-dark" x="0" y="447" width="1200" height="215" fill="#141010"/>
    <rect class="band-gold" x="0" y="662" width="1200" height="148" fill="url(#band)"/>
    <rect class="band-rule" x="0" y="810" width="1200" height="8" fill="#5a3218"/>
    <rect class="band-gold" x="0" y="818" width="1200" height="122" fill="url(#band)"/>
    <rect class="band-rule" x="0" y="940" width="1200" height="6" fill="#b98a45"/>
    <rect class="band-dark" x="0" y="946" width="1200" height="114" fill="#141010"/>
    <rect class="band-rule" x="0" y="1060" width="1200" height="8" fill="#b98a45"/>
    <polygon class="diamond-frame" points="600,58 918,482 600,906 282,482" fill="none" stroke="#e9c27a" stroke-width="8"/>
    <polygon class="diamond" points="600,72 902,482 600,892 298,482" fill="#141010"/>
    <circle class="diamond-dot" cx="600" cy="745" r="22" fill="none" stroke="#e9c27a" stroke-width="6"/>
  </svg>

  <div class="continent-area" role="img" aria-label="Gold outline of the African continent"></div>
  <span class="year year-left">20</span>
  <span class="year year-right">25</span>

  <div class="brand brand-main">GOLD</div>
  <div class="brand brand-sub">COMB</div>

  <div class="claim claim-raw">RAW</div>
  <div class="claim claim-natural">NATURAL</div>
  <div class="claim claim-organic">ORGANIC<br>CERTIFIED</div>
  <div class="claim claim-ethical">ETHICALLY<br>PRODUCED</div>

  <div class="origin">SOURCED FROM ZAMBIA’S PRISTINE<br>MIOMBO FORESTS</div>
</div>
</body>
</html>
```